名刺の表には基本情報、裏には提供サービスの概要、をデザイン頂きたく思います。
*表:基本情報
写真、キャッチフレーズ、肩書、名前、会社情報
*裏:サービス概要
(上記全て詳細は添付ファイルを確認下さい)
依頼詳細の通りです。
最新のクラウドサービスを活用する業務のため、先進的なデザインを希望します。またメインターゲットが、若手経営者となりますので、その点でもデザイン性は重要となりますので、よろしくお願いいたします。

パッと見た時の洗煉されたデザインが気に入りました。また縦名刺デザインでうまく写真を活用いただいたので、記憶に残るデザインだと思いました。ありがとうございます。

数多くのご提案をいただき、心から御礼申し上げます。今後も何卒よろしくお願いいたします。

```html
<!DOCTYPE html>
<html lang="ja">
<head>
<meta charset="utf-8">
<title>名刺デザイン 表・裏</title>
<link href="https://fonts.googleapis.com/css2?family=Noto+Sans+JP:wght@400;500;700;900&display=swap" rel="stylesheet">
<style>
:root{
  --page:#f2f2f2;
  --ink:#1e1e1e;
  --muted:#555;
  --blue:#1a8fd6;
  --blue-dark:#0d6fb3;
  --bubble:#8c8c8c;
  --yellow:#ffe600;
  --orange:#e8760a;
  --red:#d81e1e;
  --line:#bbb;
  --white:#fff;
}
*{margin:0;padding:0;box-sizing:border-box}
html,body{width:893px;height:1200px;overflow:hidden;background:var(--page);font-family:"Noto Sans JP",sans-serif;color:var(--ink)}
.side-label{position:absolute;left:30px;font-size:20px;color:var(--muted)}
.card{position:absolute;left:30px;width:833px;background:var(--white);border:1px solid #ddd;overflow:hidden}
.card-front{top:45px;height:521px}
.card-back{top:619px;height:557px}

/* front */
.catch{position:absolute;left:34px;top:105px;width:345px;font-size:26px;font-weight:900;line-height:1.6;letter-spacing:0;white-space:nowrap}
.cloud-art{position:absolute;left:70px;top:262px;width:190px;height:95px;border-radius:50px;background:linear-gradient(180deg,#e6f3fb,#c7e3f5)}
.portrait{position:absolute;left:395px;top:45px;width:235px;height:476px;background:linear-gradient(180deg,#e9eef2 0%,#c9d3dc 60%,#dfe4e8 100%)}
.vtext{position:absolute;writing-mode:vertical-rl;font-weight:700}
.specialty{right:14px;top:30px;font-size:25px;line-height:1.3;color:var(--ink)}
.role{right:96px;top:45px;font-size:15px;color:var(--muted);font-weight:500}
.name{right:120px;top:110px;font-size:50px;font-weight:900;letter-spacing:.25em}
.company{position:absolute;left:34px;top:380px;font-size:21px;font-weight:700}
.contact{position:absolute;left:34px;top:418px;font-size:13px;line-height:24px;color:#333}
.contact li{list-style:none;display:flex;align-items:center;gap:7px;white-space:nowrap}
.contact svg{width:14px;height:14px;flex:none}

/* back */
.headline{position:absolute;left:0;top:0;width:100%;height:72px;background:linear-gradient(180deg,#2aa5ea,var(--blue-dark));color:var(--white);font-size:31px;font-weight:900;display:flex;align-items:center;justify-content:center;letter-spacing:.03em}
.headline em{font-style:normal;color:var(--yellow)}
.worries{position:absolute;left:25px;top:88px;width:783px;display:flex;justify-content:space-between}
.worry{width:248px;height:100px;background:var(--bubble);color:var(--white);border-radius:14px;font-size:15px;font-weight:700;line-height:1.5;display:flex;align-items:center;justify-content:center;text-align:center;position:relative}
.worry::after{content:"";position:absolute;left:50%;bottom:-14px;margin-left:-12px;border:12px solid transparent;border-top:14px solid var(--bubble);border-bottom:0}
.invite{position:absolute;left:120px;top:212px;width:593px;height:36px;background:var(--yellow);font-size:19px;font-weight:900;display:flex;align-items:center;justify-content:center}
.invite b{color:var(--red)}
.services{position:absolute;left:25px;top:262px;width:783px;height:124px;border:2px solid var(--line);border-radius:14px;padding:10px 20px}
.services h2{font-size:19px;font-weight:900;color:var(--orange);margin-bottom:6px}
.services li{list-style:none;font-size:16px;line-height:1.6}
.examples-label{position:absolute;left:250px;top:398px;height:28px;padding:0 18px;background:var(--blue);color:var(--white);font-size:16px;font-weight:700;display:flex;align-items:center;border-radius:4px}
.examples{position:absolute;left:25px;top:436px;width:783px;font-size:16px;line-height:33px}
.examples p{border-bottom:1px dashed var(--line)}
</style>
</head>
<body>
<div class="side-label" style="top:12px">おもて</div>
<section class="card card-front">
  <p class="catch">経営者のお悩みを、<br>最新のクラウドサービスを<br>活用して、解決いたします！</p>
  <div class="cloud-art" role="img" aria-label="クラウドとダウンロード矢印のイラスト"></div>
  <div class="portrait" role="img" aria-label="タブレットを持った代表者の写真"></div>
  <p class="vtext specialty">中小企業のための<br>クラウドサービス導入支援の専門家</p>
  <p class="vtext role">代表取締役社長</p>
  <h1 class="vtext name">森田 健吾</h1>
  <p class="company">株式会社ソラリ企画</p>
  <ul class="contact">
    <li><svg viewBox="0 0 16 16"><path d="M8 1a5 5 0 0 0-5 5c0 4 5 9 5 9s5-5 5-9a5 5 0 0 0-5-5z" fill="#1a8fd6"/><circle cx="8" cy="6" r="2" fill="#fff"/></svg>〒390-0000 架空県みどり市本町1-2-3</li>
    <li><svg viewBox="0 0 16 16"><path d="M4 1h3l1 4-2 1a8 8 0 0 0 4 4l1-2 4 1v3c0 1-1 2-2 2A13 13 0 0 1 1 3c0-1 1-2 3-2z" fill="#1a8fd6"/></svg>080-0000-1234</li>
    <li><svg viewBox="0 0 16 16"><rect x="1" y="3" width="14" height="10" rx="1" fill="#1a8fd6"/><path d="M1 4l7 5 7-5" fill="none" stroke="#fff" stroke-width="1.4"/></svg>morita.kengo@sorari.example</li>
  </ul>
</section>

<div class="side-label" style="top:588px">うら</div>
<section class="card card-back">
  <h2 class="headline">こんな<em>“お悩み”</em>お持ちではありませんか？</h2>
  <div class="worries">
    <p class="worry">ＩＴには詳しくないから…<br>時間もないし…<br>どうしたらいいかわからない</p>
    <p class="worry">各種クラウドサービスを<br>使ってみたいけど、<br>どれがいいのか判断できない</p>
    <p class="worry">本当にメリットがあるの？<br>デメリットはないの？<br>専門家に聞いてみたい</p>
  </div>
  <p class="invite">そんな方はお気軽にご相談下さい！相談料はもちろん<b>無料。</b></p>
  <div class="services">
    <h2>● クラウドサービスの専門家が提供するサービス</h2>
    <ul>
      <li>・各社様の現状・問題点を分析し、最適なクラウドサービスをご提案します。</li>
      <li>・クラウドサービスの初期設定〜導入支援まで一貫してご支援いたします。</li>
      <li>・導入後のアフターケアも継続的に実施いたします。</li>
    </ul>
  </div>
  <p class="examples-label">クラウドサービスの実例</p>
  <div class="examples">
    <p>SKYBOX（データ共有）、NOTELEAF（情報共有）、チームノート LIVE（グループウェア）</p>
    <p>daylog（日報管理）、CARDPOOL（名刺管理）、BILLO（請求・見積管理）</p>
    <p>WORKCLOCK（勤怠管理）、KAIKEI クラウド（財務会計）、MEETBOX（動画配信）etc</p>
  </div>
</section>
</body>
</html>
```